Ferris Contracting LLC Business Card Design

I am looking for a creative and unique business card design. We are a commercial construction general contractor. With the name "FERRIS" Contracting, I am hoping to see some neat designs that correlate with the name.

```html
<!DOCTYPE html>
<html lang="en">
<head>
<meta charset="utf-8">
<title>Ferris Contracting LLC – Business Card</title>
<link rel="stylesheet" href="https://fonts.googleapis.com/css2?family=Lato:wght@400;700&family=Montserrat:wght@400&display=swap">
<style>
  :root {
    --backdrop: #9a9a9a;
    --card-white: #ffffff;
    --card-black: #000000;
    --brand-blue: #2a8fd6;
    --brand-blue-deep: #1c6fc0;
    --steel: #b8b8b8;
    --ink: #1a1a1a;
    --ink-soft: #333333;
  }
  html, body {
    margin: 0;
    padding: 0;
    width: 1200px;
    height: 1059px;
    overflow: hidden;
    background: var(--backdrop);
  }
  .canvas {
    position: relative;
    width: 1200px;
    height: 1059px;
  }
  .card {
    position: absolute;
    border-radius: 30px;
    overflow: hidden;
  }
  .card--front {
    left: 253px;
    top: 76px;
    width: 700px;
    height: 403px;
    background: var(--card-white);
  }
  .card--back {
    left: 242px;
    top: 567px;
    width: 723px;
    height: 413px;
    background: var(--card-black);
  }
  .brand {
    position: absolute;
    display: flex;
    align-items: center;
    gap: 10px;
    font-family: "Lato", sans-serif;
    font-weight: 700;
    color: var(--brand-blue);
    white-space: nowrap;
    letter-spacing: 1px;
  }
  .brand__dot {
    border-radius: 50%;
    background: var(--brand-blue);
    flex: none;
  }
  .card--front .brand {
    right: 44px;
    top: 88px;
    font-size: 27px;
  }
  .card--front .brand__dot { width: 18px; height: 18px; }
  .card--back .brand {
    left: 50%;
    top: 50%;
    transform: translate(-50%, -50%);
    font-size: 44px;
    letter-spacing: 2px;
    gap: 16px;
  }
  .card--back .brand__dot { width: 28px; height: 28px; }
  .person {
    position: absolute;
    left: 35px;
    top: 197px;
  }
  .person__name {
    margin: 0;
    font-family: "Lato", sans-serif;
    font-weight: 700;
    font-size: 29px;
    color: var(--brand-blue);
    letter-spacing: 0.2px;
    line-height: 1;
  }
  .person__role {
    margin: 12px 0 0;
    font-family: "Lato", sans-serif;
    font-weight: 400;
    font-size: 19px;
    color: var(--ink);
    line-height: 1;
  }
  .divider {
    position: absolute;
    left: 35px;
    top: 272px;
    width: 629px;
    height: 1px;
    background: var(--ink);
  }
  .contact {
    position: absolute;
    left: 35px;
    top: 292px;
    margin: 0;
    padding: 0;
    list-style: none;
    font-family: "Lato", sans-serif;
    font-size: 19px;
    color: var(--ink);
  }
  .contact__item {
    display: flex;
    align-items: center;
    gap: 14px;
    height: 32px;
  }
  .contact__icon { width: 21px; height: 21px; flex: none; }
  .address {
    position: absolute;
    right: 36px;
    top: 293px;
    margin: 0;
    font-family: "Montserrat", sans-serif;
    font-style: normal;
    font-size: 18px;
    line-height: 31px;
    color: var(--ink-soft);
    text-align: right;
  }
  .footer-band {
    position: absolute;
    left: 0;
    bottom: 0;
    width: 700px;
    height: 36px;
  }
  .footer-band__url {
    position: absolute;
    right: 47px;
    bottom: 7px;
    font-family: "Lato", sans-serif;
    font-size: 18px;
    color: var(--card-white);
    letter-spacing: 0.3px;
  }
</style>
</head>
<body>
<main class="canvas">

  <section class="card card--front" aria-label="Business card front">
    <div class="brand"><span class="brand__dot"></span>FERRIS CONTRACTING</div>

    <div class="person">
      <h1 class="person__name">GRANT ELSWORTH</h1>
      <p class="person__role">Managing Director</p>
    </div>

    <div class="divider"></div>

    <ul class="contact">
      <li class="contact__item">
        <svg class="contact__icon" viewBox="0 0 24 24" aria-hidden="true">
          <path fill="var(--brand-blue)" d="M6.6 10.8a15.1 15.1 0 0 0 6.6 6.6l2.2-2.2a1 1 0 0 1 1-.25 11.4 11.4 0 0 0 3.6.57 1 1 0 0 1 1 1V20a1 1 0 0 1-1 1A17 17 0 0 1 3 4a1 1 0 0 1 1-1h3.5a1 1 0 0 1 1 1c0 1.25.2 2.450.57 3.57a1 1 0 0 1-.25 1z"/>
          <path fill="none" stroke="var(--brand-blue)" stroke-width="1.6" d="M14 3.5a7 7 0 0 1 6.5 6.5M14 7a3.5 3.5 0 0 1 3 3"/>
        </svg>
        <span>044-555 218 370</span>
      </li>
      <li class="contact__item">
        <svg class="contact__icon" viewBox="0 0 24 24" aria-hidden="true">
          <rect x="2" y="5" width="20" height="14" fill="var(--brand-blue)"/>
          <path d="M2 5l10 8 10-8" fill="none" stroke="#fff" stroke-width="1.6"/>
        </svg>
        <span>info@ferrisbuild.com</span>
      </li>
    </ul>

    <address class="address">421, Address line goes here<br>45452, Country name</address>

    <svg class="footer-band" viewBox="0 0 700 36" preserveAspectRatio="none" aria-hidden="true">
      <polygon points="0,8 400,8 388,18 0,18" fill="var(--steel)"/>
      <polygon points="0,24 380,24 418,0 700,0 700,36 0,36" fill="var(--brand-blue)"/>
      <rect x="0" y="32" width="700" height="4" fill="var(--brand-blue-deep)"/>
    </svg>
    <span class="footer-band__url">www.ferrisbuild.com</span>
  </section>

  <section class="card card--back" aria-label="Business card back">
    <div class="brand"><span class="brand__dot"></span>FERRIS CONTRACTING</div>
  </section>

</main>
</body>
</html>
```